Kestrel Orchard Fliers and logo design

We need to design a product logo and some informational fliers for a pebble quest.
I have attached our Kestrel Orchard logo - colours need to be complimentary but not the same, we would like fresh, funky but still professional. We generally communicate in a fairly casual way to reach our market. (We don't like boring)
Clear and simple - not too busy
images are good but not actual photos
Here is our website to give you an idea www.kestrelorchard.co.nz
The flier is a 3 page document.
The logo is to say Pebble Quest. The challenge is based on exercise, connecting with people, giving, learning and taking notice (The 7 stones of Marlow) Once agin the logo needs to be complementary but not the same.
The Kestrel orchard logo needs to be on the fliers but the pebble quest logo is separate.
Thanks very much!!

```html
<!DOCTYPE html>
<html lang="en">
<head>
<meta charset="utf-8">
<title>Pebble Quest – Steps 2 and 3 and 10 Tips</title>
<link href="https://fonts.googleapis.com/css2?family=Arimo:wght@400;700&display=swap" rel="stylesheet">
<style>
  :root {
    --teal-deep: #036b66;
    --teal-bright: #22a98d;
    --leaf-green: #8dbd4c;
    --ember: #e0563a;
    --ink: #222222;
    --paper: #ffffff;
  }
  * { box-sizing: border-box; margin: 0; padding: 0; }
  html, body { width: 928px; height: 1200px; overflow: hidden; background: var(--paper); }
  body { font-family: "Arimo", Arial, sans-serif; color: var(--ink); position: relative; }

  .page { position: relative; width: 928px; height: 1200px; overflow: hidden; }

  .frame-art { position: absolute; inset: 0; width: 928px; height: 1200px; }

  .brand-mark { position: absolute; left: 36px; top: 46px; display: flex; align-items: center; gap: 14px; }
  .brand-mark .dot { width: 54px; height: 54px; border-radius: 50%; background: var(--teal-bright); }
  .brand-mark .name { font-size: 36px; font-weight: 700; color: var(--teal-bright); letter-spacing: 1px; }

  .partner-mark { position: absolute; left: 612px; top: 60px; display: flex; align-items: center; gap: 12px; }
  .partner-mark .dot { width: 26px; height: 26px; border-radius: 50%; background: var(--ember); }
  .partner-mark .name { font-size: 34px; font-weight: 700; color: var(--teal-bright); line-height: 1; }

  .section-title {
    position: absolute; left: 59px; color: var(--paper); font-weight: 700;
    font-size: 23px; line-height: 24px; text-transform: uppercase;
  }
  .step-two-title { top: 150px; }
  .step-three-title { top: 427px; }
  .tips-title { top: 518px; font-size: 23px; }

  .intro { position: absolute; left: 60px; top: 205px; width: 780px; font-size: 14px; line-height: 17.8px; }

  .ranked-list { position: absolute; left: 60px; top: 266px; width: 815px; list-style: none; }
  .ranked-list li { display: flex; align-items: flex-end; height: 29.5px; font-size: 16px; font-weight: 700; }
  .ranked-list li .rule { flex: 1; border-bottom: 1px solid #333; margin-left: 6px; height: 18px; }

  .support-note { position: absolute; left: 60px; top: 484px; font-size: 15.2px; }

  .tips { position: absolute; left: 94px; top: 557px; width: 790px; font-size: 14px; line-height: 17.6px; }
  .tips p.lead { margin-bottom: 7px; }
  .tip-list { list-style: none; margin-top: 6px; }
  .tip-list li { position: relative; margin-bottom: 7.6px; }
  .tip-list li strong { font-weight: 700; }
  .tip-num {
    position: absolute; left: -35px; top: -2px; width: 23px; height: 23px; border-radius: 50%;
    background: var(--ember); color: var(--paper); font-size: 12px; font-weight: 700;
    display: flex; align-items: center; justify-content: center;
    box-shadow: 0 0 0 2px var(--paper), 0 0 0 3px var(--ember);
  }
</style>
</head>
<body>
<div class="page">
  <svg class="frame-art" viewBox="0 0 928 1200" aria-hidden="true">
    <rect x="0" y="122" width="545" height="16" fill="var(--leaf-green)"/>
    <polyline points="608,0 520,168 928,168" fill="none" stroke="var(--ember)" stroke-width="4"/>
    <polygon points="0,146 464,146 532,198 0,198" fill="var(--teal-deep)"/>
    <polygon points="0,421 508,421 564,476 0,476" fill="var(--teal-deep)"/>
    <polygon points="0,514 552,514 584,545 0,545" fill="var(--teal-deep)"/>
    <rect x="0" y="1100" width="34" height="100" fill="var(--leaf-green)"/>
    <rect x="894" y="1100" width="34" height="100" fill="var(--leaf-green)"/>
    <rect x="0" y="1170" width="928" height="30" fill="var(--leaf-green)"/>
  </svg>

  <div class="brand-mark"><span class="dot"></span><span class="name">PEBBLE QUEST</span></div>
  <div class="partner-mark"><span class="dot"></span><span class="name">kestrel orchard</span></div>

  <h2 class="section-title step-two-title">Step 2:<br>Elimination</h2>
  <p class="intro">Now that you have identified ten, imagine that you are only permitted to have five values. Which five would you give up? Cross them off. Put them into order, the one that is most important to you first. Write it somewhere and refer to it when you can't make a decision, align yourself with what makes you feel good.</p>
  <ol class="ranked-list">
    <li>1.<span class="rule"></span></li>
    <li>2.<span class="rule"></span></li>
    <li>3.<span class="rule"></span></li>
    <li>4.<span class="rule"></span></li>
    <li>5.<span class="rule"></span></li>
  </ol>

  <h2 class="section-title step-three-title">Step 3:<br>Support Yourself</h2>
  <p class="support-note">Write it somewhere and refer to it when you can't make a decision, align yourself with what makes you feel good.</p>

  <h2 class="section-title tips-title">10 Tips to Improve Your Wellbeing</h2>
  <div class="tips">
    <p class="lead">Yes, you will have to get off the couch and you might need to say no to burgers for lunch every day but we promise we won't turn you into spandex wearing vegans with prescriptions to Velvetleaf!</p>
    <p class="lead">Small changes every day can make a huge difference.</p>
    <ol class="tip-list">
      <li><span class="tip-num">01</span><strong>Put on your wake up grin</strong> - Smile and think happy thoughts – that first 90 secs has a big impact on your day. If you start the day with bad thoughts, then it compounds – simply turn up the corners of your mouth you'll start to release endorphins and serotonin, your feel-good hormones.</li>
      <li><span class="tip-num">02</span><strong>Drink lemon and warm water first thing</strong> – and keep drinking water all day. It will cleanse your liver, you will eat less, you'll feel better and have a clearer head.</li>
      <li><span class="tip-num">03</span><strong>Exercise</strong> – it boosts the happy chemicals in your brain. So Be Active - get your heart rate going and stretch those muscles. At the very least take the stairs. To get your endorphins surging you'll need to really heavy breathe – so walk up those stairs faster, do your house work quicker – get that heart pumping.</li>
      <li><span class="tip-num">04</span><strong>Eat a banana</strong> – Did you ever see a depressed chimp? Bananas help to lessen feelings of stress and anxiety due to high levels of tryptophan which converts to serotonin – one of those happy hormone. The high level of potassium helps you to be more alert and will give you energy.</li>
      <li><span class="tip-num">05</span><strong>Put on your WOW! Glasses</strong> – Go outside and Take Notice – The wind, the warmth, the cold, the trees, the blossom, the amazing sky, the moon. The world is full of things that make you go WOW, if you just slow down and Take Notice. Even better, go with a friend and Connect as well.</li>
      <li><span class="tip-num">06</span><strong>5 fruit and veg per day</strong> – Get the fibre into to you… Without it you clog up, if you clog up you get grumpy and sluggish, if you get grumpy and sluggish – let's not go there! If you have trouble fitting the veges in, put them into a smoothie.</li>
      <li><span class="tip-num">07</span><strong>Play music</strong> – it cheers you up. Create a playlist for when you need a pick-me-up. Play it in the car to and from work, doing your housework or when you're going for that brisk walk, getting out of breath and send even more happy hormones to your brain. (No, not the sad break-up playlist!)</li>
      <li><span class="tip-num">08</span><strong>Remove a poison</strong> – Take away something that you know is bad for you – fast food, sugar, gluten – even for a couple of days a week – replace it with something healthy like water, fruit, veg, quinoa, exercise whatever works for you.</li>
      <li><span class="tip-num">09</span><strong>Kill em with kindness</strong> – When you're feeling bad, do something nice for someone else and it will make their day and you'll feel even better. In fact, Give every day.</li>
      <li><span class="tip-num">10</span><strong>Keep the cogs turning</strong> – Use it or lose it as they say – use your brain. Keep learning – something new every day.</li>
    </ol>
  </div>
</div>
</body>
</html>
```